Vela Errands Web Design Project

Homepage components
o Logo
o Rotating header
o Main menu
o Animation video
o Banners
o Members login
o Latest news

The design’s preferred colors are black (background), silver (main tabs) and white (text)

Site map:
• Home
• News
• About us
o Welcome Note
o Company Profile
• Member Log in
o Registered homepage
? Request a service (form)
? Services directory
? Update profile
? Services history
• Member registration
o Registration form
• Partners
Footer Menu
• Contact us
• Terms & Conditions
• Privacy policy
• Social media links
• Sitemap

Brief about the company:
Vela Errands is a Jordanian company dedicated to elevate and redefine the level of service in the country. We are set out to give premium services at affordable prices. In this fast paced environment that we live in, we barely have the luxury of free time anymore and we, at Vela Errands will be giving you that extra hour or two per day to spend as your heart desires!
By becoming a member you will get access to a world of comfort and peace of mind. We have done the homework on your behalf and have established the network of connections that will enable you to live a headache free life.
We will be providing our members with support and assistance in their day to day lives in the fields that consumes and wastes time the most. We are value driven and below is our “ever-growing” list of services that we will provide at excellent prices:
• Maintenance (carpentry, plumbing, electrical, painting, decorating, gardening… etc)
• Cleaning (pre and post tenancy, periodical deep cleaning, packing and moving services, laundry… etc)
• Personalized delivery services (grocery, important documents, office related supplies, posting cheques, food, paying bills… etc)
• Passport, driving license and ID reissuance
• Travel arrangements (flights, hotels, airport transfers… etc)
• Premium car rental services
• Restaurant reservations
• IT assistance
• Event planning and all related services
• Catering arrangements

Aside from all the services we have on offer we have collaborated with a number of places (that we like to call partners) in town where Vela Errands members are entitled to benefits and privileges that will most certainly add value to their membership. Alongside our partners we have come up with the best formula that will please our members. Below are some of our current partners:

Requirements
Must have
• Homepage components
o Logo
o Rotating header
o Main menu
o Animation video
o Banners
o Members login
o Latest news

```html
<!DOCTYPE html>
<html lang="en">
<head>
<meta charset="utf-8">
<title>Vela Errands — Home</title>
<link rel="stylesheet" href="https://fonts.googleapis.com/css2?family=Ubuntu:wght@400;500&family=Saira+Condensed:wght@400&family=Lato:wght@400&display=swap">
<style>
:root{
  --page:#231f20;
  --strip:#7a7a7a;
  --header:#d3d3d3;
  --hero:#000;
  --panel:#1b1617;
  --tab:#3d3d3b;
  --footer:#0e0e0e;
  --lime:#c8f000;
  --gold:#f0b400;
  --quote:#eadca2;
  --olive:#8d9a45;
  --text:#e6e6e6;
  --muted:#cfcfcf;
  --arrow:#7fa6d8;
}
*{box-sizing:border-box;margin:0;padding:0}
html,body{width:1200px;height:1159px;overflow:hidden}
body{position:relative;background:var(--page);font-family:"Ubuntu",sans-serif;color:var(--text)}
.abs{position:absolute}
ul{list-style:none}

.top-strip{left:0;top:0;width:1200px;height:9px;background:var(--strip)}
.share-bar{left:412px;top:17px;width:314px;height:26px;background:#fff;border-radius:6px;display:flex;align-items:center;gap:8px;padding:0 8px;font-size:11px;color:#235}
.share-btn{display:flex;align-items:center;gap:3px;border:1px solid #c9d2e0;border-radius:3px;padding:1px 5px;background:#eef2f8}
.share-btn i{width:11px;height:11px;border-radius:2px;background:#8aa0c0;display:inline-block}
.share-count{border:1px solid #ccc;padding:0 5px;color:#333;background:#fff}
.util-nav{left:979px;top:21px;display:flex;gap:16px;font-size:14px;color:#eee}
.util-nav li{display:flex;align-items:center;gap:5px}

.site-header{left:20px;top:51px;width:1161px;height:131px;background:var(--header);border-radius:8px 8px 0 0}
.brand{left:54px;top:78px;font-size:46px;font-weight:400;color:#2a2a2a;letter-spacing:1px}
.tagline{left:104px;top:128px;font-size:15px;color:#9a9a9a;letter-spacing:1px}
.search{left:846px;top:97px;width:246px;height:34px;border-radius:8px;background:#e4e8e8;font-size:14px;color:#8a9494;padding:8px 18px;letter-spacing:.5px}
.search-icon{left:1098px;top:92px}

.main-nav{left:0;top:182px;width:1200px;height:40px;background:linear-gradient(#4a4546,#141112)}
.main-nav li{position:absolute;top:11px;font-size:15px;color:#eee;letter-spacing:.6px}
.nav-sep{position:absolute;top:4px;width:1px;height:32px;background:#8a8a8a}
.new-account{left:998px;top:189px;width:183px;height:30px;border-radius:7px;background:linear-gradient(#5c5758,#2b2728);font-size:14px;color:#fff;padding:7px 0 0 48px;letter-spacing:.4px}
.lock{left:998px;top:170px}

.hero{left:98px;top:234px;width:992px;height:357px;background:var(--hero);border-radius:8px;overflow:hidden}
.hero-visual{position:absolute;right:0;top:0;width:413px;height:357px;background:radial-gradient(ellipse at 55% 45%,#8a8a8a 0%,#3a3a3a 35%,#050505 75%),#000}
.hero-visual::after{content:"";position:absolute;inset:0;background:radial-gradient(ellipse at 40% 45%,rgba(160,0,10,.55) 0%,rgba(120,0,0,0) 45%)}
.hero-title{position:absolute;left:40px;top:60px;font-family:"Saira Condensed",sans-serif;font-size:35px;color:#f2f2f2}
.hero-copy{position:absolute;left:61px;top:131px;width:540px;font-size:13.6px;line-height:22px;letter-spacing:.5px;color:#f0f0f0}
.read-more{position:absolute;left:435px;top:219px;width:134px;height:39px;border-radius:8px;background:#4a4547;color:#eee;font-size:12px;text-align:center;line-height:39px;letter-spacing:.5px}
.read-more-shadow{position:absolute;left:442px;top:262px;width:120px;height:24px;background:linear-gradient(#2a2728,#000)}
.slider-dots{left:1090px;top:421px;width:37px;height:150px;background:#1c1a1b;border:1px solid #555;border-left:none}
.slider-dots span{position:absolute;left:5px;width:22px;height:22px;border-radius:50%;background:#555}
.slider-dots .active{background:var(--lime)}
.slider-pointer{left:1080px;top:473px}

.panel{top:602px;height:364px;background:var(--panel);border-radius:8px}
.panel-tab{position:absolute;top:2px;height:37px;border-radius:8px;background:var(--tab);font-size:18px;text-align:center;line-height:37px;letter-spacing:.6px}
.tab-lime{color:var(--lime)}
.tab-silver{color:#c8c8c8;background:#464646}
.tab-gold{color:var(--gold);background:none}
.small{font-size:12px;letter-spacing:.6px;color:var(--muted);line-height:19px}
.news-item{position:absolute;left:18px;width:255px}
.news-date{display:block;text-align:right;margin-bottom:2px}
.bullet-list li{position:absolute;font-size:13px;letter-spacing:.6px;color:#eee;padding-left:20px}
.bullet-list.lime li::before{content:"";position:absolute;left:2px;top:3px;border-left:7px solid var(--lime);border-top:5px solid transparent;border-bottom:5px solid transparent}
.bullet-list.blue li::before{content:"";position:absolute;left:0;top:1px;width:12px;height:12px;background:var(--arrow);clip-path:polygon(0 0,100% 50%,0 100%,30% 50%)}
.story-quote{position:absolute;left:10px;width:240px;font-size:11.6px;line-height:14px;letter-spacing:.5px;color:var(--quote)}
.story-author{position:absolute;left:10px;font-size:12px;color:var(--quote)}
.story-rule{position:absolute;left:22px;width:208px;border-top:1px dashed #999}
.lime-mark{top:934px;height:7px;background:var(--lime)}

.site-footer{left:20px;top:966px;width:1161px;height:183px;background:var(--footer)}
.footer-col{position:absolute;top:50px}
.footer-col h3{font-family:"Lato",sans-serif;font-weight:400;font-size:24px;color:#fff;margin-bottom:16px}
.footer-col li{font-size:12px;color:var(--olive);letter-spacing:.5px;height:25px;padding-left:13px;position:relative}
.footer-col li::before{content:"›";position:absolute;left:0;top:-2px;color:#ccc;font-size:11px}
.social{position:absolute;left:914px;top:64px;width:231px;height:64px;background:#222;border-radius:8px}
.social span{position:absolute;top:16px;width:33px;height:33px;border-radius:50%}
.bottom-strip{left:0;top:1149px;width:1200px;height:10px;background:#bdbdbd}
</style>
</head>
<body>
<div class="abs top-strip"></div>

<div class="abs share-bar">
  <span class="share-btn"><i></i>post</span>
  <span class="share-btn"><i></i>Submit</span>
  <span class="share-btn"><i></i>Like</span><span class="share-count">0</span>
  <span class="share-btn">+1</span><span class="share-count">0</span>
</div>
<ul class="abs util-nav">
  <li><svg width="11" height="14"><polygon points="0,0 11,7 0,14 3,7" fill="var(--arrow)"/></svg>Login</li>
  <li><svg width="11" height="14"><polygon points="0,0 11,7 0,14 3,7" fill="var(--arrow)"/></svg>Help</li>
  <li><svg width="11" height="14"><polygon points="0,0 11,7 0,14 3,7" fill="var(--arrow)"/></svg>FAQS</li>
</ul>

<header class="abs site-header"></header>
<div class="abs brand">Vela Errands</div>
<div class="abs tagline">we make life easier</div>
<div class="abs search">Search</div>
<svg class="abs search-icon" width="42" height="42" viewBox="0 0 42 42">
  <circle cx="17" cy="17" r="12" fill="#dfeaf2" stroke="#6d8fb0" stroke-width="3"/>
  <line x1="26" y1="26" x2="38" y2="38" stroke="#444" stroke-width="6" stroke-linecap="round"/>
</svg>

<nav class="abs main-nav">
  <ul>
    <li style="left:20px">Home</li>
    <span class="nav-sep" style="left:89px"></span>
    <li style="left:104px">About us</li>
    <li style="left:210px">Member registration</li>
    <span class="nav-sep" style="left:381px"></span>
    <li style="left:408px">Partners</li>
    <span class="nav-sep" style="left:493px"></span>
    <li style="left:516px">Contact us</li>
  </ul>
</nav>
<div class="abs new-account">New Account</div>
<svg class="abs lock" width="38" height="50" viewBox="0 0 38 50">
  <path d="M9 22 V13 a10 10 0 0 1 20 0 V22" fill="none" stroke="#b8bcc0" stroke-width="5"/>
  <rect x="2" y="21" width="34" height="27" rx="4" fill="#4aa3e0"/>
  <rect x="2" y="21" width="34" height="9" rx="4" fill="#8ecbf2"/>
</svg>

<section class="abs hero">
  <div class="hero-visual" role="img" aria-label="Moody studio photograph in grey and black with a swirl of red rose petals"></div>
  <h1 class="hero-title">Vela Errands is a Jordanian company</h1>
  <p class="hero-copy">We are set out to give premium services at affordable prices. In this fast paced environment that we live in, we barely have the luxury of free time anymore and we, at Vela Errands will be giving you that extra hour or two per day to spend as your heart desires</p>
  <div class="read-more">Read More</div>
  <div class="read-more-shadow"></div>
</section>
<div class="abs slider-dots">
  <span style="top:14px"></span>
  <span class="active" style="top:46px"></span>
  <span style="top:76px"></span>
  <span style="top:108px"></span>
</div>
<svg class="abs slider-pointer" width="8" height="12"><polygon points="0,0 8,6 0,12" fill="var(--lime)"/></svg>

<section class="abs panel" style="left:20px;width:288px">
  <div class="panel-tab tab-lime" style="left:54px;width:141px">Latest News</div>
  <div class="news-item small" style="top:49px"><span class="news-date">10/10/12</span>Lorem ipsum dolor sit amet, consectetuer adipiscing</div>
  <div class="news-item small" style="top:118px"><span class="news-date">10/10/12</span>Lorem ipsum dolor sit amet, consectetuer adipiscing</div>
  <div class="news-item small" style="top:192px"><span class="news-date">10/10/12</span>Lorem ipsum dolor sit amet, consectetuer adipiscing</div>
  <div class="news-item small" style="top:273px"><span class="news-date">10/10/12</span>Lorem ipsum dolor sit amet, consectetuer adipiscing</div>
</section>

<section class="abs panel" style="left:322px;width:289px">
  <div class="panel-tab tab-lime" style="left:60px;width:172px;top:3px">Why Choose Us?</div>
  <p class="small" style="position:absolute;left:25px;top:58px;width:255px">Lorem ipsum dolor sit amet, consectetuer adipiscingLorem ipsum dolor sit amet, consectetuer adipiscingLorem ipsum dolor sit amet, consectetuer adipiscing</p>
  <ul class="bullet-list lime">
    <li style="left:38px;top:171px">Lorem ipsum dolor consectetuer</li>
    <li style="left:38px;top:196px">Adipiscing elit, diam nonummy</li>
    <li style="left:38px;top:221px">Nibh euismod tincidunt laoreet</li>
    <li style="left:38px;top:246px">Dolore magna aliquam volutpat</li>
    <li style="left:38px;top:271px">Ut wisi enim ad minim veniam</li>
  </ul>
</section>

<section class="abs panel" style="left:623px;width:289px">
  <div class="panel-tab tab-silver" style="left:51px;width:172px">Our Services</div>
  <ul class="bullet-list blue">
    <li style="left:22px;top:64px">Lorem ipsum dolor consectetuer</li>
    <li style="left:22px;top:89px">Adipiscing elit, diam nonummy</li>
    <li style="left:22px;top:114px">Nibh euismod tincidunt laoreet</li>
    <li style="left:22px;top:139px">Dolore magna aliquam volutpat</li>
    <li style="left:22px;top:164px">Ut wisi enim ad minim veniam</li>
    <li style="left:25px;top:205px">Lorem ipsum dolor consectetuer</li>
    <li style="left:25px;top:230px">Adipiscing elit, diam nonummy</li>
    <li style="left:25px;top:255px">Nibh euismod tincidunt laoreet</li>
    <li style="left:25px;top:280px">Dolore magna aliquam volutpat</li>
    <li style="left:25px;top:305px">Ut wisi enim ad minim veniam</li>
  </ul>
</section>

<section class="abs panel" style="left:923px;width:258px">
  <div class="panel-tab tab-gold" style="left:0;width:258px">Top Stories</div>
  <p class="story-quote" style="top:57px">"Lorem ipsum dolor sit amet, consectetuer adipiscing elit, sed diam nonummy."</p>
  <span class="story-author" style="top:95px">Dana Corr</span>
  <span class="story-rule" style="top:124px"></span>
  <p class="story-quote" style="top:155px;left:14px">"Lorem ipsum dolor sit amet, consectetuer adipiscing elit, sed diam nonummy."</p>
  <span class="story-author" style="top:193px;left:14px">Joud Corr</span>
  <span class="story-rule" style="top:222px;left:26px"></span>
  <p class="story-quote" style="top:254px;left:13px">"Lorem ipsum dolor sit amet, consectetuer adipiscing elit, sed diam nonummy."</p>
  <span class="story-author" style="top:292px;left:13px">Dana Corr</span>
  <span class="story-rule" style="top:321px"></span>
</section>

<span class="abs lime-mark" style="left:19px;width:2px"></span>
<span class="abs lime-mark" style="left:308px;width:14px"></span>
<span class="abs lime-mark" style="left:611px;width:12px"></span>
<span class="abs lime-mark" style="left:912px;width:11px"></span>
<span class="abs lime-mark" style="left:1180px;width:2px"></span>

<footer class="abs site-footer">
  <div class="footer-col" style="left:39px"><h3>About Us</h3><ul><li>Lorem ipsum dolo</li><li>Lorem ipsum dolo</li><li>Lorem ipsum dolo</li></ul></div>
  <div class="footer-col" style="left:206px"><h3>Advice</h3><ul><li>Lorem ipsum dolo</li><li>Lorem ipsum dolo</li><li>Lorem ipsum dolo</li></ul></div>
  <div class="footer-col" style="left:373px"><h3>Join In</h3><ul><li>Lorem ipsum dolo</li><li>Lorem ipsum dolo</li><li>Lorem ipsum dolo</li></ul></div>
  <div class="footer-col" style="left:540px"><h3>Downloads</h3><ul><li>Lorem ipsum dolo</li><li>Lorem ipsum dolo</li><li>Lorem ipsum dolo</li></ul></div>
  <div class="social" aria-label="Social media links">
    <span style="left:32px;background:#39b4e6"></span>
    <span style="left:80px;background:#34508f"></span>
    <span style="left:127px;background:#f2f2f2"></span>
    <span style="left:177px;background:#f08a12"></span>
  </div>
</footer>
<div class="abs bottom-strip"></div>
</body>
</html>
```